HarborLoop - Shore Excursions Operator Software Trade show pop-up display

Create Trade show Pop-up banners Suitable for printing at 33.5 inches by 80 inches high. I have included a description of what our software does. We are at a trade show focusing on acquiring tour operators to sign up and use our software. This specifically is built for cruise line markets. I am uploading two versions of our logo, one is just a simple version the other is the name spelled out. We want to include both because as a new company the branding identity is not very strong with the simple logo. The image I'm uploading is a backdrop with the cruise ship is what we use for our back image on the customer facing website. I am also uploading some screenshots of our software which is designed for desktop, tablet, and mobile. I want to be provocative and enticing and somewhat cutting edge but certainly to be driven towards the cruise industry and tour operators who work with the cruise industry specifically. I also uploaded an example of a chatgpt display for reference as to what we are looking for (but not that image specifically).
HarborLoop Software Overview for Designers
Purpose of the Software:
HarborLoop is an all-in-one operating system for shore excursion tour operators. It connects directly with cruise lines, manages every part of tour operations, and helps operators maximize revenue while reducing manual work.
The software is designed for companies that provide tours, transportation, and shore excursions for cruise ship passengers. Operators use HarborLoop to run their entire business — from inventory management to daily dispatch.
Key Value in Simple Terms
Maximize Revenue → By syncing with cruise ship schedules, managing contracts, invoicing, and reallocating inventory in real time.
Operational Control → From assigning guides and vehicles to monitoring maintenance and scheduling daily tours automatically.
Simplify Bookings → Manage bookings from cruise lines, travel agents, and direct guests in one hub.
Smarter Management → Staff, inventory, contracts, and content are centralized for full visibility and efficiency.
Future-Proof → Analytics, reporting, and scalability ensure operators grow alongside cruise line demand.
What HarborLoop Does (Modules & Functions)
1. Cruise Line & Revenue Management
Real-time cruise calendars
Pricing & contract management
Automated invoicing for cruise lines
Faster release of inventory for sales
Visual cues for design: 📅 Calendar icons, 💰 revenue charts, 📄 contract documents.
2. Inventory & Allocation
Central hub for inventory (direct sales, cruise lines, individual ships)
Automatic capacity alerts (when seats run low)
Bulk uploads of sales data (hundreds of hours saved)
Demand-based allocation for higher yield
Visual cues: 🚍 Bus seats filling up, ⚠️ alerts, ⬆️ demand graphs.
3. Booking & Guest Management
Unified booking system (cruise lines, agents, direct guests)
Integrated payments & invoices
Guest management for changes, cancellations, special requests
Agent & affiliate campaign tools
Visual cues: 🎟 tickets, 🧑🤝🧑 guest icons, 💳 payment/booking screens.
4. Daily Tour Dispatch (DTD)
Generates real-time daily tour schedule
Assigns guides, drivers, and vehicles automatically
Tracks guest counts & departures live
Mobile access for staff & guides
Visual cues: 🚌 bus/tour icons, 📱 mobile access, ✅ checklist/schedule view.
5. Fleet & Maintenance
Live fleet tracking (location, activity, mileage)
Inspection & maintenance reports
Photo/video upload for repair tracking
Visual cues: 🚐 vehicles, 🔧 maintenance tools, 📍 GPS markers.
6. Employee & Staff Management
Track certifications, training, and staff profiles
Assign roles, shifts, and responsibilities
Proactive alerts for expired credentials
Visual cues: 🧑✈️ staff badges, 🎓 training icons, 👤 profile cards.
7. Content & Branding Control
Manage all tour content (descriptions, itineraries, FAQs, images, videos)
Apply refund policies & contracted rates
Ensure consistent, accurate guest-facing info
Visual cues: 🖼 images, 📝 itinerary lists, 🌐 consistent branding.
8. Analytics & Future-Proofing
Sales reporting by ship, departure, and channel
Historic vs. future pricing analysis
Scalable platform that grows with the operator
Visual cues: 📊 dashboards, 📈 performance charts, 🔮 forward-looking visuals.
Overall Design Themes to Convey
Smart, seamless, and connected. (No clutter, everything integrated.)
Professional + trustworthy. (Executive decision-makers are the audience.)
Cruise-specific but modern. (Avoid cliché palm trees; instead, ships, schedules, people, and data visuals.)
Dynamic and active. (Show energy — tours, departures, real-time control.)

```html
<!DOCTYPE html>
<html lang="en">
<head>
<meta charset="utf-8">
<title>HarborLoop – Trade Show Banner</title>
<link rel="stylesheet" href="https://fonts.googleapis.com/css2?family=Roboto:wght@400;700&display=swap">
<style>
  :root{
    --page:#ececec;
    --royal:#0b3a9e;
    --royal-deep:#08307f;
    --navy:#0c2a5a;
    --mist:#e7eefb;
    --cyan:#1aa8f2;
    --white:#ffffff;
    --sunset-top:#f3a45c;
    --sunset-mid:#f6c486;
    --sea-light:#3ec1d3;
    --sea-deep:#0f6f94;
  }
  *{margin:0;padding:0;box-sizing:border-box}
  html,body{width:1200px;height:1080px;overflow:hidden;background:var(--page)}
  body{font-family:'Roboto',sans-serif;position:relative}

  .banner{position:absolute;left:383px;top:20px;width:434px;height:1040px;background:var(--royal);overflow:hidden}
  .banner__hero{position:absolute;left:0;top:0;width:434px;height:430px;
    background:linear-gradient(180deg,var(--sunset-top) 0%,var(--sunset-mid) 17%,var(--sea-light) 30%,var(--sea-deep) 62%,var(--royal-deep) 100%)}
  .banner__shape{position:absolute;left:0;top:0;width:434px;height:1040px}

  .brand-mark{position:absolute;left:22px;top:30px;display:flex;align-items:center;gap:6px;
    font-weight:700;font-size:17px;color:var(--navy)}
  .brand-mark__dot{width:14px;height:14px;border-radius:50%;background:var(--navy)}

  .tablet{position:absolute;left:114px;top:226px;width:207px;height:141px;border-radius:10px;
    background:#111;padding:6px;box-shadow:0 14px 18px rgba(0,0,0,.35)}
  .tablet__screen{width:100%;height:100%;border-radius:5px;
    background:linear-gradient(90deg,var(--navy) 0 16%,#f4f6fa 16% 100%)}

  .headline{position:absolute;left:0;top:436px;width:434px;text-align:center;color:var(--white);
    font-weight:700;font-size:39px;line-height:35px;letter-spacing:-.3px}

  .pill{position:absolute;left:161px;top:559px;width:115px;height:31px;border-radius:6px;background:var(--white);
    color:var(--navy);font-weight:700;font-size:21px;line-height:31px;text-align:center}

  .value{position:absolute;width:130px;margin-left:-65px;text-align:center;color:var(--white);font-size:14.5px;line-height:20px}
  .value svg{display:block;margin:0 auto 8px;width:46px;height:46px}

  .decor-dot{position:absolute;left:15px;top:834px;width:58px;height:58px;border-radius:50%;background:var(--royal-deep)}

  .tagline{position:absolute;left:0;top:934px;width:434px;text-align:center;color:var(--navy);
    font-weight:700;font-size:23px;line-height:21px}
  .wordmark{position:absolute;left:0;top:996px;width:434px;text-align:center;color:var(--navy);
    font-weight:700;font-size:30px;letter-spacing:.5px}
</style>
</head>
<body>
<main class="banner">
  <div class="banner__hero" role="img" aria-label="Photo of a cruise ship bow on the sea at sunset, with water splash"></div>
  <svg class="banner__shape" viewBox="0 0 434 1040" aria-hidden="true">
    <path d="M0 270 Q120 410 434 380 L434 1040 L0 1040Z" fill="var(--royal)"/>
    <path d="M0 1004 Q217 760 434 1004 L434 1040 L0 1040Z" fill="var(--mist)"/>
  </svg>

  <div class="brand-mark"><span class="brand-mark__dot"></span>HarborLoop</div>

  <div class="tablet"><div class="tablet__screen" role="img" aria-label="Software screenshot of the cruise calendar view"></div></div>

  <h1 class="headline">The Operating<br>System for Shore<br>Excursions</h1>

  <div class="pill">Key Values</div>

  <div class="value" style="left:89px;top:618px">
    <svg viewBox="0 0 48 48"><circle cx="24" cy="24" r="19" fill="none" stroke="#fff" stroke-width="2"/><circle cx="22" cy="25" r="14" fill="var(--cyan)"/><circle cx="22" cy="23" r="11" fill="#fff"/><text x="22" y="30" text-anchor="middle" font-size="17" font-weight="700" fill="var(--navy)">$</text></svg>
    Maximize Revenue</div>
  <div class="value" style="left:218px;top:618px">
    <svg viewBox="0 0 48 48"><path d="M22 4 L38 10 V24 C38 34 30 41 22 44 C14 41 6 34 6 24 V10Z" fill="none" stroke="#fff" stroke-width="2"/><circle cx="30" cy="30" r="13" fill="var(--cyan)"/><circle cx="30" cy="30" r="6" fill="none" stroke="#fff" stroke-width="2.5" stroke-dasharray="3 2"/></svg>
    Operational<br>Control</div>
  <div class="value" style="left:339px;top:618px">
    <svg viewBox="0 0 48 48"><circle cx="24" cy="38" r="10" fill="var(--cyan)"/><rect x="6" y="8" width="36" height="32" fill="none" stroke="#fff" stroke-width="2"/><line x1="6" y1="15" x2="42" y2="15" stroke="#fff" stroke-width="2"/><g fill="none" stroke="#fff" stroke-width="1.5"><rect x="10" y="19" width="6" height="5"/><rect x="21" y="19" width="6" height="5"/><rect x="32" y="19" width="6" height="5"/><rect x="10" y="29" width="6" height="5"/><rect x="32" y="29" width="6" height="5"/></g><path d="M21 31 l3 3 l4-5" stroke="#fff" stroke-width="2" fill="none"/></svg>
    Simplify Bookings</div>
  <div class="value" style="left:149px;top:762px">
    <svg viewBox="0 0 48 48"><circle cx="30" cy="20" r="12" fill="var(--cyan)"/><circle cx="30" cy="20" r="5" fill="none" stroke="#fff" stroke-width="2.5"/><circle cx="12" cy="18" r="5" fill="none" stroke="#fff" stroke-width="2.5"/><path d="M4 38 L14 32 H26 L40 30 L30 42 H12Z" fill="none" stroke="#fff" stroke-width="2"/></svg>
    Smarter<br>Management</div>
  <div class="value" style="left:280px;top:762px">
    <svg viewBox="0 0 48 48"><circle cx="32" cy="32" r="12" fill="var(--cyan)"/><path d="M20 6 L34 11 V24 C34 33 27 40 20 43 C13 40 6 33 6 24 V11Z" fill="none" stroke="#fff" stroke-width="2"/><path d="M20 18 C17 23 16 26 20 29 C24 26 23 23 20 18Z" fill="none" stroke="#fff" stroke-width="2"/><circle cx="38" cy="10" r="7" fill="none" stroke="#fff" stroke-width="2"/><path d="M35 10 l2 2 l4-4" fill="none" stroke="#fff" stroke-width="2"/></svg>
    Future-Proof</div>

  <div class="decor-dot"></div>

  <p class="tagline">Cruise Smarter. Operate<br>Stronger. Grow Faster.</p>
  <p class="wordmark">HarborLoop</p>
</main>
</body>
</html>
```